VORTAL Business Card Design

We need a business card for a new company based on the Gold Coast, we are a new supplement distributing company called VORTAL Sports Nutrition - Bold Horizon Sports Nutrition. We are providing new science based bodybuilding and fitness supplementation. Our company has a key focus towards next generation. We are wanting a card that is cool, innovative and fresh. We would like to see the implementation of the below image in a fresh and very innovative design that stands out. The final design should communicate New, Innovative, Cool, Science and researched based.
Target Market(s)
The target market is fitness and bodybuilder enthusiasts. Young audience so very cool looking.
Industry/Entity Type
Fitness
Contact Information for Business Card
(front of card)
VORTAL Sports Nutrition.
Liam Darrow
CEO/Sport Nutrition Specialist
0472 638 904
Liam@vortalsportsfuel.example
www.vortalsportsfuel.example
(back of card)
Scientifically formulated supplement range
Private Nutrition consultations
comprehensive sports nutrition seminars
Requirements
Nice to have
- The card could have a cut out on one of the sides or one of the corners rounded off so the card looks different from a normal business card.
Should not have
- The colours need to complement each other and pop out.

```html
<!DOCTYPE html>
<html lang="en">
<head>
<meta charset="utf-8">
<title>VORTAL Sports Nutrition – Business Card</title>
<link rel="stylesheet" href="https://fonts.googleapis.com/css2?family=Didact+Gothic&family=Montserrat:wght@700&display=swap">
<style>
  :root {
    --stage: #3b3c3e;
    --card-top: #0f2f40;
    --card-mid: #081722;
    --card-base: #020405;
    --brand-blue: #5cc8f2;
    --ink-white: #ffffff;
    --ink-soft: #e9f3f8;
  }
  * { box-sizing: border-box; margin: 0; padding: 0; }
  html, body {
    width: 1200px;
    height: 900px;
    overflow: hidden;
    background: var(--stage);
  }
  .canvas {
    position: relative;
    width: 1200px;
    height: 900px;
    display: flex;
    justify-content: center;
    align-items: center;
    gap: 60px;
  }
  .card {
    position: relative;
    width: 380px;
    height: 660px;
    border-radius: 4px;
    background:
      radial-gradient(ellipse 120% 60% at 50% 20%, var(--card-top) 0%, var(--card-mid) 55%, var(--card-base) 100%);
    box-shadow: 0 18px 40px rgba(0, 0, 0, 0.45);
    color: var(--ink-white);
    font-family: "Didact Gothic", "Century Gothic", sans-serif;
    text-align: center;
    overflow: hidden;
  }
  .card__texture {
    position: absolute;
    inset: 0;
    background: linear-gradient(180deg, rgba(92, 200, 242, 0.06) 0%, rgba(0, 0, 0, 0) 60%);
  }

  /* Brand wordmark */
  .wordmark {
    position: relative;
    display: flex;
    flex-direction: column;
    align-items: center;
    gap: 18px;
  }
  .wordmark__dot {
    width: 26px;
    height: 26px;
    border-radius: 50%;
    background: var(--brand-blue);
  }
  .wordmark__name {
    font-family: "Didact Gothic", "Century Gothic", sans-serif;
    color: var(--brand-blue);
    letter-spacing: 0.06em;
    line-height: 1;
  }

  /* Services side */
  .card--services .wordmark { margin-top: 130px; }
  .card--services .wordmark__name { font-size: 74px; }
  .tagline {
    position: relative;
    margin-top: 70px;
    font-size: 19px;
    letter-spacing: 0.02em;
    text-transform: uppercase;
  }
  .headline-offer {
    position: relative;
    margin-top: 56px;
    font-size: 22px;
    line-height: 1.15;
    color: var(--brand-blue);
    text-transform: uppercase;
  }
  .service-list {
    position: relative;
    list-style: none;
    margin-top: 52px;
    font-size: 21px;
    line-height: 1.15;
    text-transform: uppercase;
  }

  /* Contact side */
  .card--contact .wordmark { margin-top: 60px; gap: 14px; }
  .card--contact .wordmark__dot { width: 20px; height: 20px; }
  .card--contact .wordmark__name { font-size: 48px; }
  .company-name {
    position: relative;
    margin-top: 34px;
    font-family: "Montserrat", "Century Gothic", sans-serif;
    font-weight: 700;
    font-size: 24px;
    text-transform: uppercase;
  }
  .company-name__accent { color: var(--brand-blue); }
  .person {
    position: relative;
    margin-top: 96px;
  }
  .person__name {
    font-family: "Montserrat", "Century Gothic", sans-serif;
    font-weight: 700;
    font-size: 40px;
    color: var(--brand-blue);
    text-transform: uppercase;
    letter-spacing: 0.01em;
  }
  .person__role {
    margin-top: 4px;
    font-size: 20px;
    color: var(--ink-soft);
  }
  .contact-list {
    position: relative;
    list-style: none;
    margin-top: 56px;
    font-size: 20px;
    line-height: 1.45;
  }
  .contact-list__phone {
    font-size: 34px;
    color: var(--brand-blue);
    margin-bottom: 14px;
  }
</style>
</head>
<body>
<main class="canvas">

  <article class="card card--services">
    <div class="card__texture"></div>
    <div class="wordmark">
      <span class="wordmark__dot"></span>
      <span class="wordmark__name">VORTAL</span>
    </div>
    <p class="tagline">Bold Horizon Sports Nutrition.</p>
    <p class="headline-offer">Scientifically Formulated<br>Supplement Range</p>
    <ul class="service-list">
      <li>Private Nutrition Consultations</li>
      <li>Comprehensive Sports Nutrition</li>
      <li>Seminars</li>
    </ul>
  </article>

  <article class="card card--contact">
    <div class="card__texture"></div>
    <div class="wordmark">
      <span class="wordmark__dot"></span>
      <span class="wordmark__name">VORTAL</span>
    </div>
    <p class="company-name">Vortal <span class="company-name__accent">Sports Nutrition</span></p>
    <div class="person">
      <h1 class="person__name">Liam Darrow</h1>
      <p class="person__role">CEO/Sport Nutrition Specialist</p>
    </div>
    <ul class="contact-list">
      <li class="contact-list__phone">0472 638 904</li>
      <li>Liam@vortalsportsfuel.example</li>
      <li>www.vortalsportsfuel.example</li>
    </ul>
  </article>

</main>
</body>
</html>
```